Redfern Espresso Branding
Business Cards & Stationary Set
Professional
Dale Ostrander
Manager
1875 Heron Ridge Ave.
White Bear Lake, MN. 55110
r_fern@quillpost.net
I would like rounded corners on the business cards
Drive-thru to receive one free 12 oz. drink of choice!

```html
<!DOCTYPE html>
<html lang="en">
<head>
<meta charset="utf-8">
<title>Redfern Espresso Stationery Set</title>
<link href="https://fonts.googleapis.com/css2?family=Open+Sans:wght@400;700&display=swap" rel="stylesheet">
<style>
:root{
  --bg-top:#050d07;
  --bg-bottom:#1f4a2b;
  --forest:#4b5a3f;
  --forest-dark:#3a4731;
  --rust:#c8632a;
  --paper:#ffffff;
  --paper-shade:#e9ece6;
  --ink:#3b4435;
  --caption:#a9b9a6;
}
*{margin:0;padding:0;box-sizing:border-box}
html,body{width:1200px;height:414px;overflow:hidden}
body{
  position:relative;
  font-family:"Open Sans",sans-serif;
  background:linear-gradient(180deg,var(--bg-top) 0%,#0c2212 55%,var(--bg-bottom) 100%);
  color:var(--ink);
}
.caption{position:absolute;font-size:6px;color:var(--caption);text-align:center}
.brand{display:flex;align-items:center;gap:4px;font-weight:700;color:var(--paper);white-space:nowrap}
.brand .mark{width:10px;height:10px;background:var(--paper)}
.brand-dark{color:var(--forest)}
.brand-dark .mark{background:var(--rust)}

/* main logo */
.logo-block{position:absolute;left:250px;top:46px;width:125px;height:92px;background:var(--forest-dark);
  display:flex;align-items:center;justify-content:center;border-radius:3px}
.logo-block .brand{font-size:11px}

/* business cards */
.card{position:absolute;border-radius:10px;overflow:hidden;background:var(--paper)}
.card-front{left:120px;top:158px;width:139px;height:77px}
.card-back{left:264px;top:158px;width:139px;height:77px}
.card .band{position:absolute;left:0;right:0;top:30px;height:18px;background:var(--forest);display:flex;align-items:center;justify-content:center}
.card .band .brand{font-size:7px}
.card .band .mark{width:7px;height:7px;background:var(--rust)}
.card .contact{position:absolute;left:8px;top:7px;font-size:4.5px;line-height:1.35}
.card .contact strong{font-size:5.5px}
.card .address{position:absolute;right:8px;bottom:6px;font-size:4.5px;line-height:1.35;text-align:right}

/* coupon cards */
.coupon{position:absolute;top:274px;width:134px;height:76px;border-radius:10px;overflow:hidden}
.coupon-green{left:29px;background:var(--forest)}
.coupon-orange{left:178px;background:var(--rust)}
.coupon-white{left:326px;background:var(--paper)}
.coupon .brand{position:absolute;left:50%;top:16px;transform:translateX(-50%);font-size:7px}
.coupon-white .brand{color:var(--forest)}
.coupon-white .brand .mark{background:var(--rust)}
.coupon .offer{position:absolute;left:6px;right:6px;bottom:10px;font-size:4.5px;color:var(--paper);text-align:center}
.coupon-white .offer{color:var(--ink)}

/* letterhead */
.letterhead{position:absolute;left:538px;top:29px;width:177px;height:355px;background:var(--paper);overflow:hidden}
.letterhead svg{position:absolute;left:0;top:0}
.letterhead .sender{position:absolute;right:14px;top:14px;font-size:4px;line-height:1.4;color:var(--ink)}
.letterhead .head-brand{position:absolute;left:20px;top:44px;font-size:7px}
.letterhead .head-brand .mark{width:8px;height:8px}
.letterhead .watermark{position:absolute;left:50%;top:170px;transform:translateX(-50%);font-size:13px;font-weight:700;color:var(--paper-shade);white-space:nowrap}

/* envelopes */
.envelopes{position:absolute;left:816px;top:60px}
.env-brand{position:absolute;font-size:6px}
.env-brand .mark{width:7px;height:7px}
</style>
</head>
<body>

<div class="logo-block"><div class="brand"><span class="mark"></span>Redfern Espresso</div></div>
<p class="caption" style="left:250px;top:142px;width:125px">Logo on dark ground</p>

<div class="card card-front">
  <div class="contact"><strong>Dale Ostrander</strong><br>Manager</div>
  <div class="band"><div class="brand"><span class="mark"></span>Redfern Espresso</div></div>
  <div class="address">1875 Heron Ridge Ave.<br>White Bear Lake, MN. 55110<br>r_fern@quillpost.net</div>
</div>
<div class="card card-back">
  <div class="contact"><strong>Dale Ostrander</strong><br>Manager</div>
  <div class="band" style="background:var(--rust)"><div class="brand"><span class="mark" style="background:var(--forest)"></span>Redfern Espresso</div></div>
  <div class="address">1875 Heron Ridge Ave.<br>White Bear Lake, MN. 55110<br>r_fern@quillpost.net</div>
</div>
<p class="caption" style="left:120px;top:240px;width:139px">Business card front</p>
<p class="caption" style="left:264px;top:240px;width:139px">Business card back</p>

<div class="coupon coupon-green"><div class="brand"><span class="mark"></span>Redfern Espresso</div><p class="offer">Drive-thru to receive one free 12 oz. drink of choice!</p></div>
<div class="coupon coupon-orange"><div class="brand"><span class="mark"></span>Redfern Espresso</div><p class="offer">Drive-thru to receive one free 12 oz. drink of choice!</p></div>
<div class="coupon coupon-white"><div class="brand"><span class="mark"></span>Redfern Espresso</div><p class="offer">Drive-thru to receive one free 12 oz. drink of choice!</p></div>
<p class="caption" style="left:29px;top:356px;width:134px">Coupon card green</p>
<p class="caption" style="left:178px;top:356px;width:134px">Coupon card orange</p>
<p class="caption" style="left:326px;top:356px;width:134px">Coupon card white</p>

<div class="letterhead">
  <svg width="177" height="355" viewBox="0 0 177 355">
    <rect x="0" y="0" width="10" height="355" fill="var(--forest)"/>
    <path d="M10 0 C18 60 18 120 12 355 L10 355 Z" fill="var(--rust)"/>
  </svg>
  <div class="sender">1875 Heron Ridge Ave.<br>White Bear Lake, MN. 55110<br>r_fern@quillpost.net</div>
  <div class="brand brand-dark head-brand"><span class="mark"></span>Redfern Espresso</div>
  <div class="watermark">Redfern Espresso</div>
</div>
<p class="caption" style="left:538px;top:388px;width:177px">Letterhead</p>

<div class="envelopes">
  <svg width="360" height="330" viewBox="0 0 360 330">
    <g transform="rotate(8 240 90)">
      <rect x="100" y="20" width="250" height="115" fill="var(--paper)"/>
      <path d="M100 20 L350 20 L350 40 Q225 95 100 40 Z" fill="var(--rust)"/>
    </g>
    <g transform="rotate(-3 180 160)">
      <rect x="40" y="85" width="270" height="120" fill="var(--paper)"/>
      <path d="M40 85 L310 85 L175 150 Z" fill="var(--paper-shade)"/>
    </g>
    <rect x="0" y="195" width="300" height="125" fill="var(--forest)"/>
    <path d="M0 320 L300 320 L300 300 Q150 250 0 300 Z" fill="var(--forest-dark)"/>
  </svg>
  <div class="brand env-brand" style="left:165px;top:42px;color:var(--paper)"><span class="mark"></span>Redfern Espresso</div>
  <div class="brand env-brand" style="left:12px;top:210px"><span class="mark"></span>Redfern Espresso</div>
</div>
<p class="caption" style="left:816px;top:388px;width:300px">Envelope</p>

</body>
</html>
```